MGC Business Card Design

I am a wedding and event Planner. I have just completed a name change from Soirees by Lucette to The Gathering Corner and I just received my new logo and need new business cards to match my new brand. Elegant, chic and upscale yet simple. I am drafting a new website on my old (for drafting purposes). You can take a look and it will give you an idea of the direction of my brand. (www.soireesbylucette.example). I would like gray and white colors and it can be a shaded mixture of grays. I am open in regard to placement of the information

Target Market(s)

Brides, Corporate Companies, Families etc.

Industry/Entity Type

Wedding

Contact Information for Business Card

The Gathering Corner
www.mygatheringcorner.example
Event Planning and Design Firm
Lucette M. Harlow, Owner/CEO
Certified Event & Wedding Planner
T: (555) 214-7390 | F: (555) 307-4128
E: wegather@mygatheringcorner.example
(please put T, E & F letters in a script font)

Love to Plan. Plan to Live. Live to Love. (lh)

(social icons instead of text)
twitter: @gatheringcorner1
facebook: @thegatheringcorner
Pinterest: @gatheringcorner
instagram: @thegatheringcorner1

Can we put a barcode leading to my website

```html
<!DOCTYPE html>
<html lang="en">
<head>
<meta charset="utf-8">
<title>The Gathering Corner – Business Card</title>
<link rel="stylesheet" href="https://fonts.googleapis.com/css2?family=Great+Vibes&family=Montserrat:wght@300;400&family=Open+Sans:wght@400;600&display=swap">
<style>
  :root {
    --page: #e4e4e2;
    --card: #ffffff;
    --ink: #5f5f5f;
    --ink-soft: #777777;
    --rule: #8a8a8a;
    --icon: #6a6a6a;
  }
  * { box-sizing: border-box; margin: 0; padding: 0; }
  html, body { width: 1200px; height: 900px; overflow: hidden; }
  body {
    background: var(--page);
    font-family: "Open Sans", Arial, sans-serif;
    color: var(--ink);
    position: relative;
  }
  .card {
    position: absolute;
    left: 250px;
    width: 700px;
    height: 400px;
    background: var(--card);
    box-shadow: 0 6px 18px rgba(0,0,0,0.18);
  }
  .card--back { top: 30px; }
  .card--front { top: 470px; }

  .mark {
    position: absolute;
    border: 3px solid var(--ink);
    border-radius: 50%;
    display: flex;
    align-items: center;
    justify-content: center;
    font-family: "Montserrat", Arial, sans-serif;
    font-weight: 300;
    color: var(--ink);
  }
  .card--back .mark {
    width: 210px; height: 210px;
    left: 245px; top: 80px;
    font-size: 46px; letter-spacing: 6px;
  }
  .card--front .mark {
    width: 110px; height: 110px;
    left: 40px; top: 50px;
    font-size: 24px; letter-spacing: 3px;
  }
  .back-url {
    position: absolute;
    right: 40px; bottom: 36px;
    font-family: "Montserrat", Arial, sans-serif;
    font-weight: 300;
    font-size: 15px;
    letter-spacing: 2px;
    color: var(--ink-soft);
  }

  .brand-name {
    position: absolute;
    left: 168px; top: 88px;
    font-family: "Montserrat", Arial, sans-serif;
    font-weight: 300;
    font-size: 26px;
    letter-spacing: 3px;
    text-transform: uppercase;
    color: var(--ink);
    white-space: nowrap;
  }
  .holder {
    position: absolute;
    left: 60px; top: 272px;
  }
  .holder__name { font-size: 25px; font-weight: 600; color: var(--ink); }
  .holder__title { font-size: 16px; color: var(--ink-soft); margin-left: 64px; }

  .divider {
    position: absolute;
    left: 432px; top: 190px;
    width: 1.5px; height: 170px;
    background: var(--rule);
  }
  .contact {
    position: absolute;
    left: 458px; top: 168px;
    width: 222px;
    font-size: 13px;
    line-height: 22px;
    color: var(--ink);
  }
  .contact__line { white-space: nowrap; }
  .contact__key {
    font-family: "Great Vibes", cursive;
    font-size: 18px;
    display: inline-block;
    width: 16px;
  }
  .contact__rule { height: 1.5px; background: var(--rule); margin: 4px 0 8px; }
  .social { list-style: none; font-size: 14px; line-height: 24px; }
  .social__item { display: flex; align-items: center; gap: 8px; white-space: nowrap; }
  .social__icon { width: 14px; height: 14px; background: var(--icon); border-radius: 2px; flex: none; }
</style>
</head>
<body>
  <section class="card card--back">
    <div class="mark">MGC</div>
    <p class="back-url">www.mygatheringcorner.example</p>
  </section>

  <section class="card card--front">
    <div class="mark">MGC</div>
    <h1 class="brand-name">The Gathering Corner</h1>

    <div class="holder">
      <p class="holder__name">Lucette M. Harlow</p>
      <p class="holder__title">Owner/CEO</p>
    </div>

    <div class="divider"></div>

    <div class="contact">
      <p class="contact__line"><span class="contact__key">T</span> (555) 214-7390</p>
      <p class="contact__line"><span class="contact__key">F</span> (555) 307-4128</p>
      <p class="contact__line"><span class="contact__key">E</span> wegather@mygatheringcorner.example</p>
      <div class="contact__rule"></div>
      <ul class="social">
        <li class="social__item"><span class="social__icon"></span>@gatheringcorner1</li>
        <li class="social__item"><span class="social__icon"></span>@thegatheringcorner</li>
        <li class="social__item"><span class="social__icon"></span>@gatheringcorner</li>
        <li class="social__item"><span class="social__icon"></span>@thegatheringcorner1</li>
      </ul>
    </div>
  </section>
</body>
</html>
```